Web site - 5-8 page

We are a small, fresh pasta business called The Noodle Harbor located in suburbs of Sacramento, CA. We sell our pasta, ravioli, meatballs and sauce at farmer's markets, events, and soon in our café & marketplace. (Jan 2014) . We also provide catering services. The site needs to communicate FRESH, local, no preservatives, artisan quality pasta. We offer vegetarian, vegan and gluten free products as well.

We would like a web site using our logos and colors to feature what we do, and where people can come buy it. A page to our standard take and make items/menu, our seasonal take and make menu, our catering menu, our new hot food café menu.

We want a page that we can update with "Where can you find The Noodle Harbor"
A "specials page" and a page they can order from that they choose the location to pick it up or in the delivery area we deliver to them.
A page with photo's and referrals, testimony, comments, about us, etc. Maybe a page for recipes.
We need to update the events/find us page all the time, weekly, so it needs to be easy for us to go in and do that. We are Window's (not MAC) users if that makes a difference or not, not sure.

Ideally, the same person(s) that make the website would also do a separate project creating our catering and hot food menu brochure/layout and recipe cards
Updates

I would like to see the landing page have the pasta shapes/sizes element that is found in the refrigerator wrap, the wrap on the trailer, and the menu - see photo and uploads. It's used as a banner or as a background, bright green.

                                   

 

Would like visitors to be able to "like" me or follow me from my web page. A button or a link?

                                        http://www.brightlarder-example.com/our-food/

Really like the layout of this site. More grocery oriented than café, but we are a take and make marketplace as well as a Panini salads and hot pasta menu for lunch.

Please add Café + Marketplace to headers. Our logo is good but we are now adding a café element and a fresh marketplace, se we need to communicate what we are/what we do. We think adding Café + Marketplace as a descriptor will help. Any ideas, feel free to put your own spin on it. Thank you!!

The designs are good...thanks to everyone!

Target Market(s)

#1, busy mom's, busy family's (FAST, Economical meals, no preservatives, local food)
#2 24-34 yr olds that want fresh, vegetarian, vegan or gluten free meal options (no preservatives, local food)
#3 Fresh pasta lovers - any age. The enjoyment of quality fresh pasta and a good meal experience sharing it with friends and family

Industry/Entity Type

Catering

Font styles to use
Other font styles liked:
• EideticNeoRegular, duffy

Colors
9bcb3c
f78f20
eb1f27

Requirements
Must have
• Address, phone, name, logo, colors
Fresh pasta, ravioli, sauce and meatballs in take and make convenient packages. Stress fresh, preservative free, local ingredients, cooks in 45 SECONDS to 3.5 minutes depending on the pasta cut.
FAST meal
Where to find us page - upcoming events
A "specials" page
A page for recipe, how to cook our pasta, how to freeze and store fresh pasta,
How to order online page
Nice to have
• Testimony, links to Facebook, twitter, etc. Place for photo's of product, recent events, customer comments on how they used the product to create their recipe.
Should not have
• No stock photo's of tomato's, no dried pasta images, no Italian flags. No cheesy old world Italian loo or feel. Think fresh, modern, FAST!

```html
<!DOCTYPE html>
<html lang="en">
<head>
<meta charset="utf-8">
<title>The Noodle Harbor – Café + Marketplace</title>
<link rel="stylesheet" href="https://fonts.googleapis.com/css2?family=Questrial&family=Lusitana&family=Lato:wght@400;700&family=Satisfy&display=swap">
<style>
:root{
  --cream:#f8f5ea;
  --green:#8dc63f;
  --green-bright:#9bcb3c;
  --green-dark:#4b7a0d;
  --lime:#c8e86a;
  --red:#eb1f27;
  --red-script:#e0262c;
  --brown:#5a3510;
  --ink:#333;
  --ink-soft:#444;
  --footer-ink:#1d2a0c;
  --panel:#e9eceb;
  --panel-line:#cfd4d2;
  --caption:rgba(28,28,28,.82);
}
*{margin:0;padding:0;box-sizing:border-box}
html,body{width:1143px;height:1200px;overflow:hidden}
body{background:var(--cream);font-family:'Lato',sans-serif;color:var(--ink);position:relative}
h2,h3{font-weight:400}

/* Sidebar */
.sidebar{position:absolute;left:138px;top:0;width:240px}
.sidebar-topbar{height:6px;background:var(--red)}
.menu-title{margin-top:12px;height:46px;background:var(--green-bright);font-family:'Questrial',sans-serif;font-size:27px;color:#1e2a10;text-align:center;line-height:46px}
.menu-group{height:38px;background:var(--panel);border-bottom:1px solid var(--panel-line);border-top:1px solid #f6f7f7;font-family:'Lusitana',serif;font-size:18px;color:#222;line-height:37px;padding-left:32px;position:relative}
.menu-group::before{content:"";position:absolute;left:16px;top:14px;width:9px;height:9px;background:#555;clip-path:polygon(50% 0,100% 25%,100% 75%,50% 100%,0 75%,0 25%)}
.menu-list{background:var(--panel);list-style:none;padding:8px 0;border-bottom:1px solid var(--panel-line);height:344px}
.menu-list li{font-family:'Lusitana',serif;font-size:13.5px;color:#444;height:26px;line-height:26px;padding-left:39px;position:relative}
.menu-list li::before{content:"";position:absolute;left:24px;top:10px;width:6px;height:6px;border-radius:50%;background:#666}

.special{position:absolute;left:138px;top:609px;width:240px;height:193px;background:var(--green-dark);padding:8px}
.special-frame{border:2px solid #b9d98a;border-radius:4px;height:100%;color:#fff;position:relative}
.special-head{font-family:'Questrial',sans-serif;line-height:1;position:absolute}
.special-week{font-size:21px;left:24px;top:20px}
.special-title{font-size:34px;left:10px;top:40px;letter-spacing:-.5px}
.special-off{right:8px;top:13px;font-size:30px;text-align:right;letter-spacing:-.5px}
.special-off span{display:block;font-size:27px}
.special-copy{position:absolute;left:12px;top:82px;right:10px;font-size:12px;line-height:15px}
.special-link{position:absolute;left:0;right:0;bottom:10px;text-align:center;font-family:'Questrial',sans-serif;font-weight:700;font-size:15px;color:var(--lime)}

/* Content */
.intro{position:absolute;left:409px;top:-10px;width:580px;font-size:14.6px;line-height:18.8px;color:var(--ink-soft)}
.read-more{position:absolute;left:898px;top:101px;font-size:12.5px;color:var(--red);text-decoration:underline}
.section-title{position:absolute;font-family:'Satisfy',cursive;font-size:25px;color:var(--red-script)}
.card{position:absolute;width:275px;height:173px;border-radius:11px;overflow:hidden;box-shadow:0 1px 3px rgba(0,0,0,.35)}
.card-photo{position:absolute;inset:0}
.card-caption{position:absolute;left:0;right:0;bottom:0;height:37px;background:var(--caption);font-family:'Questrial',sans-serif;font-size:20px;color:var(--lime);text-align:center;line-height:37px}
.col-a{left:408px}.col-b{left:711px}

/* Lower info */
.info-title{position:absolute;font-family:'Satisfy',cursive;font-size:26px;color:#111}
.badge{position:absolute;width:86px;height:86px;border-radius:50%;border:4px solid #fff;box-shadow:0 3px 5px rgba(0,0,0,.35);display:flex;align-items:center;justify-content:center}
.badge-green{background:var(--green-bright)}
.badge-brown{background:var(--brown)}
.product{position:absolute;left:245px;top:886px;width:345px;font-size:14.5px;line-height:17px;color:#111;font-weight:700}
.product b{color:var(--red-script)}
.product-desc{position:absolute;left:245px;top:934px;width:330px;font-size:12.8px;line-height:16px;color:var(--ink-soft)}
.testimonial{position:absolute;left:725px;top:885px;width:265px;font-size:12.8px;line-height:16px;color:var(--ink-soft)}
.testimonial p+p{margin-top:15px}
.pill{position:absolute;height:29px;border-radius:15px;background:var(--green-bright);border:1px solid #6e9e1e;font-size:13px;color:#222;text-align:center;line-height:27px}

/* Footer */
.footer{position:absolute;left:0;top:1020px;width:1143px;height:180px}
.footer-band{position:absolute;inset:0}
.footer-nav{position:absolute;left:0;right:0;top:1058px;text-align:center;font-size:14.6px;color:var(--footer-ink);word-spacing:1px}
.footer-nav span{margin:0 8px}
.contact{position:absolute;top:1105px;font-size:12.8px;line-height:15.6px;color:var(--footer-ink)}
.contact-social{width:195px}
.social{position:absolute;top:1113px;width:40px;height:40px;border-radius:50%}
</style>
</head>
<body>

<aside class="sidebar">
  <div class="sidebar-topbar"></div>
  <h2 class="menu-title">Our Menu</h2>
  <div class="menu-group">Fresh Pasta</div>
  <ul class="menu-list">
    <li>Basil</li><li>Black Pepper</li><li>Buckwheat Egg Garlic</li><li>Gluten-Free</li>
    <li>Herb</li><li>Lemon</li><li>Pumpkin</li><li>Red Chili Pepper</li>
    <li>Roasted Sweet Red Pepper</li><li>Saffron</li><li>Spinach</li>
    <li>Squid Ink (black pasta)</li><li>Whole Wheat</li>
  </ul>
  <div class="menu-group">Fresh Ravioli</div>
  <div class="menu-group">Fresh Gnocchi</div>
  <div class="menu-group">Fresh Tortellini</div>
  <div class="menu-group">Fresh Sauces</div>
</aside>

<section class="special">
  <div class="special-frame">
    <div class="special-head special-week">This week</div>
    <div class="special-head special-title">SpeciaL</div>
    <div class="special-head special-off">20%<span>LESS</span></div>
    <p class="special-copy">Lorem ipsum dolor sit amet, consectetur adipiscing elit. Integer tempus elementum sagittis, dime ntum, ipsum eu consequat</p>
    <div class="special-link">KNOW MORE</div>
  </div>
</section>

<p class="intro">Beciegast nveriti vitaesaert asety kertya aset aplica boserde nerafae kertyuraestyasnemo faserani iasera ptaiadeser daesraeds. Casrolern atur aut oditaut. onsequuntur magni dolqui ratione voluptatemsequi nesciunt orasario numquam eius modi teincidunt, ut labore et dolore magnam lijaseras. Beciegast nveriti vitaesaert asety kertya aset aplica boserde nerafae kertyuraestyasnemo faserani iasera ptaiadeser daesraeds.</p>
<span class="read-more">Read More</span>

<h3 class="section-title" style="left:410px;top:122px">Our Favorite</h3>
<div class="card col-a" style="top:169px">
  <div class="card-photo" role="img" aria-label="Photo of spaghetti with tomato sauce and a glass of red wine" style="background:linear-gradient(160deg,#5a1a12 0%,#b5361f 45%,#d9a25a 70%,#3a1a10 100%)"></div>
  <div class="card-caption">Pasta with Sauce</div>
</div>
<div class="card col-b" style="top:169px">
  <div class="card-photo" role="img" aria-label="Photo of fresh pasta with green beans in a white bowl" style="background:linear-gradient(170deg,#e8edf0 0%,#f2f2ee 35%,#d8b878 60%,#8aa84a 80%,#c9cfd2 100%)"></div>
  <div class="card-caption">Fresh Pasta with Beans</div>
</div>

<h3 class="section-title" style="left:420px;top:352px">Fresh Pasta with Salad</h3>
<div class="card col-a" style="top:399px">
  <div class="card-photo" role="img" aria-label="Photo of penne with chicken, tomatoes and herbs" style="background:linear-gradient(150deg,#2a1d14 0%,#7a4a2a 30%,#d9b070 55%,#a8321c 75%,#3a2818 100%)"></div>
  <div class="card-caption">Chicken Pasta</div>
</div>
<div class="card col-b" style="top:399px">
  <div class="card-photo" role="img" aria-label="Photo of pasta salad with cucumber, olives and peppers in a glass bowl" style="background:linear-gradient(160deg,#c9d4c2 0%,#efe6b4 35%,#9dbb55 60%,#e8dca0 80%,#b8c6b6 100%)"></div>
  <div class="card-caption">Pasta Salad</div>
</div>

<h3 class="section-title" style="left:420px;top:578px">Ready To Cook</h3>
<div class="card col-a" style="top:628px">
  <div class="card-photo" role="img" aria-label="Photo of stir-fried noodles in a dark bowl with chopsticks" style="background:linear-gradient(165deg,#f0ede6 0%,#c89a62 35%,#8a5a2e 60%,#1f1a16 100%)"></div>
  <div class="card-caption">10 minute to cook</div>
</div>
<div class="card col-b" style="top:628px">
  <div class="card-photo" role="img" aria-label="Photo of spaghetti with meatballs in tomato sauce" style="background:linear-gradient(160deg,#e9e4dc 0%,#c24a22 35%,#8a2a14 60%,#d88a3a 85%,#b33a20 100%)"></div>
  <div class="card-caption">Juicy Meatalls</div>
</div>

<h3 class="info-title" style="left:244px;top:836px">Pasta Types</h3>
<div class="badge badge-green" style="left:145px;top:877px">
  <svg width="36" height="32" viewBox="0 0 36 32" aria-hidden="true"><path d="M18 31 C6 22 1 16 1 9.5 1 4.5 5 1 9.8 1 13.5 1 16.5 3.2 18 6 19.5 3.2 22.5 1 26.2 1 31 1 35 4.5 35 9.5 35 16 30 22 18 31Z" fill="#fff"/></svg>
</div>
<p class="product"><b>Valley Mill Grains Whole Grain Bucatini</b> 8.50 lb / 7.00 12 oz.</p>
<p class="product-desc">Hard amber durum, whole grain wheat flour (by Valley Mill grains), water.</p>
<div class="pill" style="left:240px;top:979px;width:133px">Explore Our Pastas</div>

<h3 class="info-title" style="left:719px;top:836px">Testimonial</h3>
<div class="badge badge-brown" style="left:625px;top:877px">
  <svg width="40" height="40" viewBox="-20 -20 40 40" aria-hidden="true">
    <g fill="#fff">
      <ellipse cx="0" cy="-10" rx="5" ry="9"/>
      <ellipse cx="0" cy="-10" rx="5" ry="9" transform="rotate(72)"/>
      <ellipse cx="0" cy="-10" rx="5" ry="9" transform="rotate(144)"/>
      <ellipse cx="0" cy="-10" rx="5" ry="9" transform="rotate(216)"/>
      <ellipse cx="0" cy="-10" rx="5" ry="9" transform="rotate(288)"/>
    </g>
    <circle r="3.5" fill="#5a3510"/>
  </svg>
</div>
<div class="testimonial">
  <p>Cyatsvitae eryas nemerat niptalas ecaerat iades metrase kaystas miausases.</p>
  <p>Cyatsvitae eryas nemerat niptalas ecaerat iades metrase kaystas miausases.</p>
</div>
<div class="pill" style="left:723px;top:979px;width:134px">More Testimonial</div>

<footer class="footer">
  <svg class="footer-band" width="1143" height="180" viewBox="0 0 1143 180" aria-hidden="true">
    <defs>
      <pattern id="zigzag" width="16" height="10" patternUnits="userSpaceOnUse">
        <polygon points="0,10 8,0 16,10" fill="#8dc63f"/>
      </pattern>
    </defs>
    <rect x="0" y="0" width="1143" height="10" fill="url(#zigzag)"/>
    <rect x="0" y="10" width="1143" height="170" fill="#8dc63f"/>
  </svg>
</footer>
<nav class="footer-nav">Catering Services<span>|</span>Cafe Menu<span>|</span>Marketplace Menu<span>|</span>Fresh Pasta<span>|</span>Location Hours<span>|</span>Friends Club<span>|</span>Our Blog<span>|</span>Contact Us</nav>
<p class="contact" style="left:167px">Stay connected to the Harbor:<br>916.555.0148<br>Marla@noodleharbor-example.com<br>©2013, All Rights Reserved,Noodle Harbor, Cafe &amp; Marketplace</p>
<p class="contact contact-social" style="left:539px">@FreshNoodleHarbor<br>https://www.fb-example.com/The<br>NoodleHarbor</p>
<span class="social" style="left:750px;background:#5fc3e4" aria-label="Social link"></span>
<span class="social" style="left:802px;background:#ef5a4e" aria-label="Social link"></span>
<span class="social" style="left:854px;background:#3b5aa0" aria-label="Social link"></span>
<span class="social" style="left:906px;background:#f4a93b" aria-label="Social link"></span>
<span class="social" style="left:953px;background:#d0202a" aria-label="Social link"></span>

</body>
</html>
```